Modern Design Business Card industrial maintenance company

Business card design for Company named Brookvale Equipment Services

Target Market(s)

Industrial

Industry/Entity Type

Maintenance and repair

Contact Information for Business Card

Place holder for address, office phone, mobile number and email

Requirements
Must have
• Clean modern look
Nice to have
• N/a

```html
<!DOCTYPE html>
<html lang="en">
<head>
<meta charset="utf-8">
<title>Brookvale Equipment Services – Business Card</title>
<link href="https://fonts.googleapis.com/css2?family=Montserrat:wght@400;600;700&display=swap" rel="stylesheet">
<style>
  :root {
    --backdrop: #6b6b6a;
    --card: #181818;
    --ink: #ffffff;
    --ink-soft: #e6e6e6;
  }
  * { box-sizing: border-box; margin: 0; padding: 0; }
  html, body { width: 1200px; height: 801px; overflow: hidden; }
  body {
    background: var(--backdrop);
    font-family: "Montserrat", sans-serif;
    color: var(--ink);
    display: flex;
    align-items: center;
    justify-content: center;
    gap: 50px;
  }
  .card {
    width: 520px;
    height: 297px;
    background: var(--card);
    position: relative;
    box-shadow: 0 10px 28px rgba(0,0,0,.35);
  }

  /* Back: brand + contact */
  .card--back { display: flex; }
  .card--back .brand-panel {
    width: 55%;
    display: flex;
    flex-direction: column;
    align-items: center;
    justify-content: center;
    gap: 14px;
  }
  .divider {
    position: absolute;
    left: 55%;
    top: 0;
    width: 1.5px;
    height: 62%;
    background: var(--ink);
  }
  .contact-panel {
    width: 45%;
    padding: 30px 0 0 18px;
  }
  .person-name {
    font-weight: 700;
    font-size: 17px;
    letter-spacing: .5px;
  }
  .person-role {
    font-size: 12px;
    color: var(--ink-soft);
    margin: 3px 0 10px;
  }
  .contact-list { list-style: none; }
  .contact-list li {
    display: flex;
    align-items: center;
    gap: 6px;
    font-size: 12px;
    line-height: 19px;
    color: var(--ink-soft);
  }
  .contact-list svg { width: 10px; height: 10px; flex: none; }
  .address {
    font-size: 12px;
    line-height: 18px;
    color: var(--ink-soft);
    margin-top: 6px;
  }

  /* Brand lockup */
  .brand-mark {
    border: 2px solid var(--ink);
    border-radius: 50%;
  }
  .brand-name {
    font-weight: 600;
    text-align: center;
    text-transform: uppercase;
    line-height: 1.1;
  }
  .brand-name .line-main { display: block; letter-spacing: 2px; }
  .brand-name .line-sub { display: block; letter-spacing: 3.5px; }

  .card--back .brand-mark { width: 70px; height: 70px; }
  .card--back .line-main { font-size: 22px; }
  .card--back .line-sub { font-size: 8.5px; margin-top: 3px; }

  /* Front: large brand */
  .card--front {
    display: flex;
    flex-direction: column;
    align-items: center;
    justify-content: center;
    gap: 18px;
  }
  .card--front .brand-mark { width: 110px; height: 110px; border-width: 3px; }
  .card--front .line-main { font-size: 36px; }
  .card--front .line-sub { font-size: 13px; letter-spacing: 6px; margin-top: 5px; }
</style>
</head>
<body>

  <section class="card card--back">
    <div class="brand-panel">
      <div class="brand-mark"></div>
      <p class="brand-name">
        <span class="line-main">Brookvale</span>
        <span class="line-sub">Equipment Services</span>
      </p>
    </div>
    <div class="divider"></div>
    <div class="contact-panel">
      <p class="person-name">DANIEL CARVER</p>
      <p class="person-role">Managing Director</p>
      <ul class="contact-list">
        <li>
          <svg viewBox="0 0 10 10"><path d="M2 1h2l1 2.5-1.3.8a5 5 0 0 0 2 2l.8-1.3L9 6v2a1 1 0 0 1-1 1A7 7 0 0 1 1 2a1 1 0 0 1 1-1z" fill="#fff"/></svg>
          123 456 789
        </li>
        <li>
          <svg viewBox="0 0 10 10"><rect x="2.5" y="0.5" width="5" height="9" rx="1" fill="none" stroke="#fff"/></svg>
          123 456 789
        </li>
        <li>
          <svg viewBox="0 0 10 10"><rect x="0.5" y="2" width="9" height="6" fill="none" stroke="#fff"/><path d="M.5 2 5 5.5 9.5 2" fill="none" stroke="#fff"/></svg>
          info@brookvalemail.com
        </li>
        <li>
          <svg viewBox="0 0 10 10"><circle cx="5" cy="5" r="4.5" fill="#fff"/></svg>
          www.brookvale-es.com
        </li>
      </ul>
      <p class="address">Your address, City<br>State, Zip 1234</p>
    </div>
  </section>

  <section class="card card--front">
    <div class="brand-mark"></div>
    <p class="brand-name">
      <span class="line-main">Brookvale</span>
      <span class="line-sub">Equipment Services</span>
    </p>
  </section>

</body>
</html>
```